Pagebook Ads for HOA Law Firm

We need to create certain ads for a Pagebook ads campaign. We are a law firm in Florida that represents homeowners against HOAs. We need to create the following ads:

1. Image Ads Specifications:

File Type: JPG or PNG
Ratio: 1.91:1 to 4:5
Resolution:
a) 1:1 ratio: 1080 x 1080 pixels
b) 4:5 ratio: 1080 x 1350 pixels
Maximum File Size: 30MB
Minimum Width: 600 pixels
Minimum Height:
a) 1:1 ratio: 600 pixels
b) 4:5 ratio: 750 pixels
Key Elements to Include in the Ads:

1) Headline: "HOA Violating Your Rights?"
2) Main Message: "We sue HOAs for Homeowners."
3) Firm Name: Lindqvist Harrow, P.A.
4) Website: www.covenantshieldcounsel.example
5) Phone Number: 1-800-555-0148
6) Florida Bar Compliance Statement: "Serving Homeowners in Florida with our main office in Miami-Dade."
7) Call-to-Action (CTA): Include a strong CTA such as “Contact us today for a consultation!”
8) Tone and Style: Professional yet approachable. The ad should emphasize trust, expertise, and our dedication to homeowners' rights.
9) Branding: Please use our firm's brand colors and fonts. Ensure that our logo is prominently placed within the ad.
10) Image Suggestions: Consider using images of Florida homes, frustrated homeowners, or visuals that evoke trust, protection, and legal authority.

```html
<!DOCTYPE html>
<html lang="en">
<head>
<meta charset="utf-8">
<title>HOA Violating Your Rights? – Lindqvist Harrow, P.A.</title>
<link rel="stylesheet" href="https://fonts.googleapis.com/css2?family=Oswald:wght@300;400;500;600;700&display=swap">
<style>
  :root {
    --navy: #0d1287;
    --panel: #e6e7e9;
    --white: #ffffff;
    --sky-top: #3b7be0;
    --sky-mid: #7fb0ea;
    --house: #d9d6cf;
    --lawn: #5d9a3a;
    --suit: #2a3a66;
  }
  * { margin: 0; padding: 0; box-sizing: border-box; }
  html, body { width: 1200px; height: 1200px; overflow: hidden; background: var(--panel); }
  .ad {
    position: relative;
    width: 1200px;
    height: 1200px;
    overflow: hidden;
    font-family: "Oswald", "Arial Narrow", sans-serif;
    background: var(--panel);
  }
  .hero-photo {
    position: absolute; left: 0; top: 0; width: 1200px; height: 842px;
    background: linear-gradient(180deg, var(--sky-top) 0%, var(--sky-mid) 38%, var(--house) 62%, #c9c6bd 82%, var(--lawn) 100%);
  }
  .attorneys-photo {
    position: absolute; left: 530px; top: 360px; width: 670px; height: 482px;
    background: linear-gradient(180deg, rgba(120,110,100,0.55) 0%, var(--suit) 70%);
    border-radius: 200px 200px 0 0;
  }
  .panel { position: absolute; left: 0; top: 0; width: 1200px; height: 1200px; }
  .headline {
    position: absolute; left: 108px; top: 110px;
    color: var(--white); font-weight: 600; font-size: 114px; line-height: 118px;
    text-transform: uppercase; letter-spacing: -1px;
    text-shadow: 0 2px 10px rgba(0,0,0,0.35);
  }
  .subline {
    position: absolute; left: 106px; top: 355px;
    color: var(--white); font-weight: 400; font-size: 56px; line-height: 70px;
    text-transform: uppercase; letter-spacing: -1px;
    text-shadow: 0 2px 8px rgba(0,0,0,0.35);
  }
  .firm-name {
    position: absolute; right: 104px; top: 166px;
    color: var(--navy); font-weight: 500; font-size: 20px; letter-spacing: 0.5px;
  }
  .consult {
    position: absolute; left: 0; width: 1200px; top: 700px; text-align: center;
    color: var(--navy); font-weight: 400; font-size: 44px; line-height: 60px; text-transform: uppercase; letter-spacing: -0.5px;
  }
  .cta {
    position: absolute; left: 307px; top: 789px; width: 590px; height: 91px;
    border-radius: 46px; background: var(--navy);
    display: flex; align-items: center; justify-content: center; gap: 28px;
    color: var(--white); font-weight: 600; font-size: 58px; text-transform: uppercase; letter-spacing: -0.5px;
  }
  .phone {
    position: absolute; left: 0; width: 1200px; top: 905px;
    display: flex; align-items: center; justify-content: center; gap: 16px;
    color: var(--navy); font-weight: 600; font-size: 68px; line-height: 80px; letter-spacing: -1px;
  }
  .service-area {
    position: absolute; left: 0; width: 1200px; top: 1010px;
    display: flex; align-items: center; justify-content: center; gap: 12px;
    color: var(--navy); font-weight: 400; font-size: 31px; line-height: 42px; text-transform: uppercase; letter-spacing: -0.3px;
  }
  .website {
    position: absolute; left: 0; width: 1200px; top: 1066px;
    display: flex; align-items: center; justify-content: center; gap: 12px;
    color: var(--navy); font-weight: 500; font-size: 31px; line-height: 42px; letter-spacing: -0.3px;
  }
  .frame { position: absolute; left: 0; top: 0; width: 1200px; height: 1200px; pointer-events: none; }
</style>
</head>
<body>
<main class="ad">
  <div class="hero-photo" role="img" aria-label="Photo of a two-storey Florida home with garage, palm shrubs and lawn under a blue sky"></div>
  <div class="attorneys-photo" role="img" aria-label="Photo of the firm's two attorneys in suits smiling"></div>

  <svg class="panel" viewBox="0 0 1200 1200" aria-hidden="true">
    <polygon points="0,838 597,602 1200,842 1200,1200 0,1200" fill="var(--panel)"/>
  </svg>

  <svg class="frame" viewBox="0 0 1200 1200" aria-hidden="true">
    <polyline points="278,838 55,838 55,56 1144,56 1144,838 925,838" fill="none" stroke="var(--navy)" stroke-width="11"/>
  </svg>

  <h1 class="headline">HOA Violating<br>Your Rights?</h1>
  <p class="subline">We sue HOAs for homeowners</p>
  <p class="firm-name">LINDQVIST HARROW, P.A.</p>

  <p class="consult">For a consultation!</p>
  <div class="cta">
    <span>Contact us today</span>
    <svg width="72" height="66" viewBox="0 0 72 66" aria-hidden="true">
      <g stroke="var(--white)" stroke-width="4" stroke-linecap="round">
        <line x1="26" y1="2" x2="26" y2="14"/>
        <line x1="4" y1="22" x2="16" y2="22"/>
        <line x1="10" y1="8" x2="17" y2="15"/>
        <line x1="42" y1="8" x2="35" y2="15"/>
        <line x1="10" y1="36" x2="17" y2="29"/>
      </g>
      <path d="M24 22 L66 40 L50 44 L62 58 L55 64 L43 50 L34 62 Z" fill="var(--white)"/>
    </svg>
  </div>

  <p class="phone">
    <svg width="68" height="68" viewBox="0 0 68 68" aria-hidden="true">
      <circle cx="34" cy="34" r="34" fill="var(--navy)"/>
      <path d="M22 16c2-1 4-1 5 1l4 8c1 2 0 4-1 5l-3 2c2 5 6 9 11 11l2-3c1-1 3-2 5-1l8 4c2 1 2 3 1 5l-2 4c-2 3-6 4-10 2-10-4-18-12-22-22-2-4-1-8 2-10z" fill="var(--panel)"/>
    </svg>
    <span>1-800-555-0148</span>
  </p>

  <p class="service-area">
    <svg width="32" height="34" viewBox="0 0 32 34" aria-hidden="true">
      <circle cx="16" cy="16" r="16" fill="var(--navy)"/>
      <path d="M16 7a7 7 0 0 0-7 7c0 5 7 12 7 12s7-7 7-12a7 7 0 0 0-7-7z" fill="var(--panel)"/>
      <circle cx="16" cy="14" r="3" fill="var(--navy)"/>
    </svg>
    <span>Serving homeowners in Florida with our main office in Miami-Dade</span>
  </p>

  <p class="website">
    <svg width="32" height="32" viewBox="0 0 32 32" aria-hidden="true" fill="none" stroke="var(--navy)" stroke-width="2">
      <circle cx="16" cy="16" r="14"/>
      <ellipse cx="16" cy="16" rx="6" ry="14"/>
      <line x1="2" y1="16" x2="30" y2="16"/>
      <line x1="5" y1="9" x2="27" y2="9"/>
      <line x1="5" y1="23" x2="27" y2="23"/>
    </svg>
    <span>www.covenantshieldcounsel.example</span>
  </p>
</main>
</body>
</html>
```